Innovative Healthcare Technology Company needs a Business Card Design

We are in need of an innovative business card design for a new healthcare software company called "Lumenwise Data Partners". We develop software that creates medical assessment applications and mobile e-learning prevention services to reduce risk behaviors in adolescent and young adults. Our initial product, the "KESTREL App", conducts a tailored sexual risk assessment and provides a doctor with an insightful patient report to improve sexual risk counseling and ultimately reduce unintended pregnancy, STDs, etc.

We would like the design to incorporate our logo and branding colors (attached) in an innovative and creative manner. The final design should communicate professionalism and healthcare innovation. Our tag line is "Foresight is the best care" (doesn't necessarily need to be included) and our target audience is doctors, medical directors, and medical business administrators. Please visit our website for additional info ourbrightmarq.com. Be creative and we look forward to seeing your designs!

Target Market(s)

healthcare - doctors, medical directors and medical business administrators

Industry/Entity Type

Healthcare

Contact Information for Business Card

We would like the design to incorporate our logo and branding colors (attached) in an innovative and creative manner. The final design should communicate professionalism and healthcare innovation. Our tag line is "Foresight is the best care" (doesn't necessarily need to be included)

Font styles to use
Other font styles liked:
• quicksand

Requirements
Must have
• our logo and brand colors
• Name, (Mara Feldhovenik, PhD)
• Email (drmara@ourbrightmarq.com)
• phone (555.283.9170)
• Website (ourbrightmarq.com)
Should not have
• cartoon look

```html
<!DOCTYPE html>
<html lang="en">
<head>
<meta charset="utf-8">
<title>Lumenwise Data Partners – Business Card</title>
<link rel="stylesheet" href="https://fonts.googleapis.com/css2?family=Quicksand:wght@500&family=Ubuntu:wght@400;500&display=swap">
<style>
  :root {
    --backdrop: #8a8c8c;
    --brand-blue: #024b85;
    --brand-green: #5f8b7e;
    --brand-grey: #9a9ba0;
    --card-light: #e2e3e7;
    --tag-white: #eef0f3;
    --text-white: #ffffff;
  }
  * { box-sizing: border-box; margin: 0; padding: 0; }
  html, body { width: 1200px; height: 900px; overflow: hidden; }
  body {
    background: var(--backdrop);
    font-family: "Ubuntu", sans-serif;
    position: relative;
  }
  .card {
    position: absolute;
    left: 321px;
    width: 507px;
    height: 290px;
    box-shadow: 0 12px 20px rgba(0,0,0,0.28);
  }
  .card--front { top: 119px; background: var(--brand-blue); }
  .card--back  { top: 471px; background: var(--card-light); }

  .tagline {
    position: absolute;
    left: 279px; top: 228px;
    width: 198px; height: 35px;
    background: var(--tag-white);
    border-radius: 2px;
    color: var(--brand-blue);
    font-size: 15px;
    font-weight: 500;
    white-space: nowrap;
    display: flex; align-items: center; justify-content: center;
  }

  .brand {
    position: absolute;
    right: 34px; top: 40px;
    display: flex; align-items: center; gap: 12px;
  }
  .brand__square {
    width: 24px; height: 24px;
    background: var(--brand-blue);
  }
  .brand__name {
    font-family: "Quicksand", sans-serif;
    font-weight: 500;
    font-size: 22px;
    color: var(--brand-blue);
    letter-spacing: 0.4px;
    white-space: nowrap;
  }

  .tab {
    position: absolute;
    left: 17px;
    border-radius: 4px;
    color: var(--text-white);
    display: flex; align-items: center;
    padding-left: 10px;
    white-space: nowrap;
  }
  .tab--name {
    top: 129px; width: 195px; height: 32px;
    background: var(--brand-grey);
    font-size: 17.5px;
  }
  .tab--name small { font-size: 12.5px; margin-left: 4px; margin-top: 3px; }
  .tab--title {
    top: 165px; width: 221px; height: 32px;
    background: var(--brand-green);
    font-size: 14.5px;
  }
  .tab--contact {
    top: 200px; width: 249px; height: 75px;
    background: var(--brand-blue);
    flex-direction: column; align-items: flex-start; justify-content: center;
    gap: 4px;
    font-size: 13px;
  }
  .contact-line { display: flex; align-items: center; gap: 8px; }
  .contact-line svg { width: 15px; height: 15px; flex: none; }
</style>
</head>
<body>

<section class="card card--front" aria-label="Card front">
  <p class="tagline">Foresight is the best care</p>
</section>

<section class="card card--back" aria-label="Card back">
  <div class="brand">
    <span class="brand__square"></span>
    <span class="brand__name">Lumenwise Data Partners</span>
  </div>

  <p class="tab tab--name">Mara Feldhovenik,<small>PhD</small></p>
  <p class="tab tab--title">CEO/Founder</p>

  <div class="tab tab--contact">
    <p class="contact-line">
      <svg viewBox="0 0 16 16" aria-hidden="true"><rect width="16" height="16" rx="3" fill="#fff"/><path d="M5 3.5l1.6 2.4-1 1c.6 1.3 1.6 2.3 2.9 2.9l1-1 2.4 1.6-.8 1.8c-3.8-.3-6.6-3.1-6.9-6.9z" fill="#024b85"/></svg>
      555.283.9170
    </p>
    <p class="contact-line">
      <svg viewBox="0 0 16 16" aria-hidden="true"><rect width="16" height="16" rx="3" fill="#fff"/><rect x="3.5" y="5" width="9" height="6.5" rx="1" fill="#024b85"/><path d="M3.8 5.4L8 8.6l4.2-3.2" stroke="#fff" stroke-width="1" fill="none"/></svg>
      drmara@ourbrightmarq.com
    </p>
    <p class="contact-line">
      <svg viewBox="0 0 16 16" aria-hidden="true"><rect width="16" height="16" rx="3" fill="#fff"/><circle cx="8" cy="8" r="4.5" fill="none" stroke="#024b85" stroke-width="1.3"/><path d="M3.5 8h9M8 3.5c-2 2.4-2 6.6 0 9M8 3.5c2 2.4 2 6.6 0 9" stroke="#024b85" stroke-width="1" fill="none"/></svg>
      www.ourbrightmarq.com
    </p>
  </div>
</section>

</body>
</html>
```